Business Cards for company that supports physicians that do medical research

Need to create a business card for oKV Lumenta (www.okvlumenta.example), a company devoted to supporting physicians who conduct medical research. The form of the card should match the message of research and information quest. I have provided the logo of the company as an uploaded file. Designs should be simple and slick aimed at very high end clients.

Target Market(s)

Medical doctors that are also researchers

Industry/Entity Type

Medical

Contact Information for Business Card

Should feature logo and fields for personal info:
Name/title
Phone /email

Font styles to use
Serif
Sans Serif

Requirements
Must have
• oKV logo and fields for personal info:
• Name: Bartholomew Okonji
• Title: VP Research and Senior Analyst
• Phone: 418-372-9146
• email: info@okvlumenta.example
Nice to have
• Interesting cards that I've seen:
• 1- all black/charcoal or very dark background
• 2- Plastic - semi-transparent
• 3- non-standard height-width ratios
• 4- Functional cards -- USB drive incorporated
Should not have
• Too busy; needs to stay very simple

```html
<!DOCTYPE html>
<html lang="en">
<head>
<meta charset="utf-8">
<title>oKV Lumenta business cards</title>
<link rel="stylesheet" href="https://fonts.googleapis.com/css2?family=Comfortaa:wght@400;700&family=Roboto+Condensed:wght@400&family=Tinos:wght@400;700&display=swap">
<style>
:root{
  --blue:#2b8fd6;
  --green:#4db848;
  --ink:#111;
  --black:#000;
  --white:#fff;
  --silver:#a9a9a9;
  --faint:#1d1d1d;
  --swoosh:#4a4a4a;
}
*{margin:0;padding:0;box-sizing:border-box}
html,body{width:1200px;height:2517px;overflow:hidden;background:var(--white)}
.sheet{display:grid;grid-template-columns:600px 600px;grid-template-rows:repeat(7,359.57px);width:1200px;height:2517px}
.card{position:relative;overflow:hidden;border-right:1px solid #333;border-bottom:1px solid #333}
.card.dark{background:var(--black);color:var(--white);border-color:#1a1a1a}
.card.gradient{background:linear-gradient(#2a2a2a,#050505)}
.card.light{background:var(--white);color:var(--ink);border-color:#555}
.abs{position:absolute}
.logo{position:absolute;display:flex;align-items:center;gap:8px;font-family:"Comfortaa",sans-serif;font-weight:700;font-size:23px;color:var(--green);white-space:nowrap}
.logo .dot{width:13px;height:13px;border-radius:50%;background:var(--blue)}
.logo.small{font-size:19px}
.logo.small .dot{width:11px;height:11px}
.logo.silver{color:var(--silver)}
.logo.silver .dot{background:var(--silver)}
.ghost{position:absolute;font-family:"Comfortaa",sans-serif;font-weight:700;color:var(--faint);white-space:nowrap}
.name{font-family:"Comfortaa",sans-serif;font-weight:700;font-size:24px;color:var(--blue);white-space:nowrap;line-height:1}
.name.white{color:var(--white)}
.title{font-family:"Roboto Condensed",sans-serif;font-size:14px;margin-top:4px;white-space:nowrap}
.title.grey{color:#777}
.contact{font-family:"Tinos",serif;font-size:12.5px;line-height:21px;white-space:nowrap}
.contact b{font-weight:700}
.contact.green{color:var(--green)}
.contact.right{text-align:right}
.contact.big{font-size:15px;line-height:27px}
.strip{position:absolute;font-family:"Tinos",serif;color:var(--green);white-space:nowrap}
.strip.phone{left:24px;top:205px;font-size:8.5px}
.strip.mail{left:366px;top:201px;font-size:11.5px}
.vrule{position:absolute;left:266px;top:91px;width:1px;height:175px;background:#555}
svg.shape{position:absolute;left:0;top:0}
</style>
</head>
<body>
<main class="sheet">

  <section class="card dark gradient">
    <div class="logo" style="left:85px;top:160px"><span class="dot"></span>oKV Lumenta</div>
    <div class="abs" style="left:303px;top:117px">
      <div class="name">Bartholomew Okonji</div>
      <div class="title">VP Research and Senior Analyst</div>
    </div>
    <div class="abs contact" style="left:303px;top:186px">Phone : 418-372-9146<br>email : info@okvlumenta.example<br>www.okvlumenta.example</div>
  </section>
  <section class="card dark gradient">
    <div class="logo silver" style="left:200px;top:160px;font-size:30px"><span class="dot"></span>oKV Lumenta</div>
  </section>

  <section class="card dark">
    <div class="logo" style="left:50px;top:88px"><span class="dot"></span>oKV Lumenta</div>
    <div class="ghost" style="left:50px;top:245px;font-size:23px;color:#2a2a2a">oKV Lumenta</div>
    <div class="abs" style="right:52px;top:112px;text-align:right">
      <div class="name white">Bartholomew Okonji</div>
      <div class="title">VP Research and Senior Analyst</div>
    </div>
    <div class="abs contact right" style="right:52px;top:210px;line-height:22.5px"><b>Phone :</b> 418-372-9146<br><b>email :</b> info@okvlumenta.example<br>www.okvlumenta.example</div>
  </section>
  <section class="card dark">
    <div class="ghost" style="left:100px;top:120px;font-size:60px">oKV Lumenta</div>
    <div class="logo small" style="left:228px;top:160px"><span class="dot"></span>oKV Lumenta</div>
    <div class="strip phone">Phone : 418-372-9146 &nbsp; www.okvlumenta.example</div>
    <div class="strip mail">email : info@okvlumenta.example</div>
  </section>

  <section class="card dark">
    <svg class="shape" width="600" height="360" viewBox="0 0 600 360" aria-hidden="true">
      <path d="M0,358 Q320,300 600,40 L600,85 Q340,310 0,358 Z" fill="var(--swoosh)"/>
    </svg>
    <div class="logo" style="left:38px;top:58px"><span class="dot"></span>oKV Lumenta</div>
    <div class="ghost" style="left:398px;top:295px;font-size:19px;color:#262626">oKV Lumenta</div>
    <div class="abs" style="left:38px;top:146px">
      <div class="name">Bartholomew Okonji</div>
      <div class="title">VP Research and Senior Analyst</div>
    </div>
    <div class="abs contact green" style="left:38px;top:217px;line-height:22.5px"><b>Phone :</b> 418-372-9146<br><b>email :</b> info@okvlumenta.example<br>www.okvlumenta.example</div>
  </section>
  <section class="card dark">
    <div class="logo small" style="left:228px;top:160px"><span class="dot"></span>oKV Lumenta</div>
    <div class="strip phone">Phone : 418-372-9146 &nbsp; www.okvlumenta.example</div>
    <div class="strip mail">email : info@okvlumenta.example</div>
  </section>

  <section class="card dark">
    <div class="logo small" style="left:85px;top:165px"><span class="dot"></span>oKV Lumenta</div>
    <div class="vrule"></div>
    <div class="abs" style="left:303px;top:117px">
      <div class="name">Bartholomew Okonji</div>
      <div class="title">VP Research and Senior Analyst</div>
    </div>
    <div class="abs contact green" style="left:303px;top:182px;line-height:22.5px"><b>Phone :</b> 418-372-9146<br><b>email :</b> info@okvlumenta.example<br>www.okvlumenta.example</div>
  </section>
  <section class="card dark">
    <div class="logo" style="left:225px;top:160px"><span class="dot"></span>oKV Lumenta</div>
  </section>

  <section class="card light">
    <div class="logo" style="left:85px;top:160px"><span class="dot"></span>oKV Lumenta</div>
    <div class="abs" style="left:303px;top:117px">
      <div class="name">Bartholomew Okonji</div>
      <div class="title">VP Research and Senior Analyst</div>
    </div>
    <div class="abs contact" style="left:303px;top:185px">Phone : 418-372-9146<br>email : info@okvlumenta.example<br>www.okvlumenta.example</div>
  </section>
  <section class="card light">
    <div class="logo" style="left:225px;top:160px"><span class="dot"></span>oKV Lumenta</div>
  </section>

  <section class="card light">
    <svg class="shape" width="600" height="360" viewBox="0 0 600 360" aria-hidden="true">
      <path d="M0,356 Q330,300 600,38 L600,88 Q350,305 0,356 Z" fill="var(--swoosh)"/>
      <path d="M0,356 Q340,295 600,60" fill="none" stroke="#222" stroke-width="2"/>
    </svg>
    <div class="logo small" style="left:55px;top:66px"><span class="dot"></span>oKV Lumenta</div>
    <div class="abs" style="left:243px;top:85px">
      <div class="name">Bartholomew Okonji</div>
      <div class="title grey">VP Research and Senior Analyst</div>
    </div>
    <div class="abs contact right big" style="right:50px;top:242px"><b>Phone :</b> 418-372-9146<br><b>email :</b> info@okvlumenta.example<br><b>www.okvlumenta.example</b></div>
  </section>
  <section class="card light">
    <div class="logo" style="left:225px;top:160px"><span class="dot"></span>oKV Lumenta</div>
  </section>

  <section class="card light">
    <svg class="shape" width="600" height="360" viewBox="0 0 600 360" aria-hidden="true">
      <defs>
        <linearGradient id="band" x1="0" x2="1">
          <stop offset="0" stop-color="#222"/><stop offset="0.5" stop-color="#aaa"/><stop offset="1" stop-color="#222"/>
        </linearGradient>
      </defs>
      <path d="M0,138 Q300,235 600,138 L600,152 Q300,225 0,160 Z" fill="url(#band)"/>
      <path d="M0,160 Q300,226 600,152" fill="none" stroke="#000" stroke-width="5"/>
    </svg>
    <div class="logo small" style="left:108px;top:66px"><span class="dot"></span>oKV Lumenta</div>
    <div class="abs" style="left:295px;top:82px">
      <div class="name">Bartholomew Okonji</div>
      <div class="title grey">VP Research and Senior Analyst</div>
    </div>
    <div class="abs contact big" style="left:0;width:600px;top:222px;text-align:center;padding-right:8px"><b>Phone :</b> 418-372-9146<br><b>email :</b> info@okvlumenta.example<br><b>www.okvlumenta.example</b></div>
  </section>
  <section class="card light">
    <div class="logo" style="left:225px;top:160px"><span class="dot"></span>oKV Lumenta</div>
  </section>

</main>
</body>
</html>
```